practice letterhead

I need a letterhead design for a new company that is a veterinary specialty company. I am conservative. I want it to look professional - not "cutesy"

I need my name, credentials, address, phone number and website/email on it.

My personal information is as follows: Marisol Tedder, DVM, DACVIM (Neurology) Certified Veterinary Pain Practitioner (or CVPP) Certified Canine Rehabilitation Therapist (or CCRT) 4170 Larkfield Hwy Fernridge, MA 01846 508-347-6620 marisol.tedder@petspineandcare.com www.petspineandcare.com

```html
<!DOCTYPE html>
<html lang="en">
<head>
<meta charset="utf-8">
<title>Practice Letterhead – Marisol Tedder</title>
<link href="https://fonts.googleapis.com/css2?family=Lato:wght@300;400;700&display=swap" rel="stylesheet">
<style>
  :root {
    --canvas-bg: #ffffff;
    --sheet-bg: #ececec;
    --navy: #122a3d;
    --green: #5fae82;
    --ink: #1f1f1f;
    --rule: #2f5a74;
    --white: #ffffff;
  }
  * { margin: 0; padding: 0; box-sizing: border-box; }
  html, body {
    width: 1200px;
    height: 1000px;
    overflow: hidden;
    background: var(--canvas-bg);
    font-family: "Lato", Arial, sans-serif;
  }
  .letterhead {
    position: absolute;
    left: 250px;
    top: 74px;
    width: 705px;
    height: 899px;
    background: var(--sheet-bg);
    box-shadow: 4px 4px 5px rgba(0,0,0,0.55);
    overflow: hidden;
  }
  .corner-sweep {
    position: absolute;
    left: 0;
    top: 0;
    width: 705px;
    height: 899px;
  }
  .brand {
    position: absolute;
    left: 62px;
    top: 88px;
    display: flex;
    align-items: center;
    gap: 14px;
  }
  .brand-dot {
    width: 62px;
    height: 62px;
    border-radius: 50%;
    background: var(--navy);
  }
  .brand-name {
    color: var(--green);
    font-weight: 700;
    font-size: 21px;
    line-height: 1.15;
    letter-spacing: 0.3px;
  }
  .header-rule {
    position: absolute;
    left: 65px;
    top: 211px;
    width: 581px;
    height: 1px;
    background: var(--rule);
  }
  .signatory {
    position: absolute;
    left: 48px;
    top: 705px;
  }
  .signatory-name {
    display: inline-block;
    color: var(--green);
    font-weight: 400;
    font-size: 26px;
    letter-spacing: -0.5px;
    padding-bottom: 1px;
    border-bottom: 1px solid var(--green);
  }
  .credentials {
    margin-top: 8px;
    color: var(--ink);
    font-weight: 400;
    font-size: 11.5px;
    line-height: 16.5px;
    letter-spacing: -0.2px;
  }
  .contact-band {
    position: absolute;
    left: 0;
    bottom: 0;
    width: 705px;
    height: 75px;
    background: var(--green);
    display: flex;
    align-items: center;
    justify-content: center;
    color: var(--white);
    font-weight: 700;
    font-size: 11.5px;
    letter-spacing: -0.3px;
    white-space: nowrap;
    padding-bottom: 12px;
  }
  .contact-band .sep { margin: 0 4px; }
</style>
</head>
<body>
  <div class="letterhead">
    <svg class="corner-sweep" viewBox="0 0 705 899" aria-hidden="true">
      <path d="M455,0 H705 V270 L702,270 C702,120 620,4 455,0 Z" fill="var(--navy)"/>
    </svg>

    <div class="brand">
      <div class="brand-dot"></div>
      <div class="brand-name">Pet Spine &amp; Care<br>Specialists</div>
    </div>

    <div class="header-rule"></div>

    <div class="signatory">
      <div class="signatory-name">Marisol Tedder</div>
      <div class="credentials">
        DVM, DACVIM (Neurology)<br>
        Certified Veterinary Pain Practitioner<br>
        Certified Canine Rehabilitation Therapist
      </div>
    </div>

    <div class="contact-band">
      4170 Larkfield Hwy Fernridge, MA<span class="sep">|</span>01846 508-347-6620<span class="sep">|</span>marisol.tedder@petspineandcare.com<span class="sep">|</span>www.petspineandcare.com
    </div>
  </div>
</body>
</html>
```